Brightpath Orthodontics business card design

Need a business card design that reflects our re-branding (orthodontic office - braces) and a new partnership with a pediatric dental office. We would like to include "for adults and children" on the card as well so adults know they are welcome to get their braces here as well. Office design is modern and would like business card to reflect a modern type look. Here's the text we would like to be included on the card:

Darren Holloway, DDS, MSD
5214 West Maple Avenue, Suite 204
Mansfield, TX 76099
817-555-0143
www.brightpathortho.example
info@brightpathortho.example
Updates

Can we add the following to the existing designs? Darren Holloway, DDS, MSD 5214 West Maple Avenue, Suite 204 Mansfield, TX 76099 817-555-0143

Does anyone have any more vertical designs available? Thanks!

Industry/Entity Type

Dental

```html
<!DOCTYPE html>
<html lang="en">
<head>
<meta charset="utf-8">
<title>Brightpath Orthodontics – Business Card</title>
<link rel="stylesheet" href="https://fonts.googleapis.com/css2?family=Exo+2:wght@500;600;700;800&display=swap">
<style>
  :root {
    --backdrop: #d9d4cc;
    --card: #262626;
    --yellow: #f5e90f;
    --blue: #1a73c4;
    --magenta: #e2147d;
    --green: #8cc63f;
    --orange: #f7941d;
    --white: #ffffff;
    --tooth: #eceef0;
  }
  * { box-sizing: border-box; margin: 0; padding: 0; }
  html, body {
    width: 1200px; height: 900px; overflow: hidden;
    background: var(--backdrop);
    font-family: "Exo 2", sans-serif;
  }
  .stage {
    width: 1200px; height: 900px;
    display: flex; align-items: center; justify-content: center;
  }
  .card {
    position: relative;
    width: 440px; height: 770px;
    background: var(--card);
    border-radius: 18px;
    overflow: hidden;
  }
  .edge-stripe {
    position: absolute; left: 0; top: 0; bottom: 0; width: 16px;
    display: flex; flex-direction: column;
  }
  .edge-stripe span { display: block; }
  .edge-stripe .yellow  { background: var(--yellow);  height: 150px; }
  .edge-stripe .blue    { background: var(--blue);    height: 150px; }
  .edge-stripe .magenta { background: var(--magenta); height: 130px; }
  .edge-stripe .green   { background: var(--green);   height: 130px; }
  .edge-stripe .orange  { background: var(--orange);  flex: 1; }

  .brand {
    position: absolute; left: 50px; top: 50px; right: 30px;
    display: flex; align-items: center; gap: 20px;
  }
  .tooth-art {
    width: 100px; height: 110px; flex: none;
    border-radius: 40px 40px 30px 30px;
    background: radial-gradient(circle at 40% 35%, #ffffff, var(--tooth) 55%, #b9bcc0);
  }
  .brand-name {
    color: var(--white);
    font-weight: 800;
    font-size: 40px;
    line-height: 1.05;
  }

  .doctor { position: absolute; left: 50px; top: 270px; }
  .doctor-name {
    color: var(--yellow);
    font-weight: 800; font-size: 31px;
    text-transform: uppercase; letter-spacing: 0.5px;
  }
  .doctor-credentials {
    color: var(--white); font-weight: 600; font-size: 17px; margin-top: 2px;
  }

  .contact { position: absolute; left: 50px; top: 365px; list-style: none; }
  .contact li {
    display: flex; align-items: center; gap: 12px;
    color: var(--white); font-weight: 600; font-size: 20px;
    margin-bottom: 8px;
  }
  .contact svg { width: 18px; height: 18px; flex: none; }

  .address {
    position: absolute; left: 50px; top: 495px;
    color: var(--orange); font-weight: 700; font-size: 21px; line-height: 1.3;
    font-style: normal;
  }
</style>
</head>
<body>
<main class="stage">
  <article class="card">
    <div class="edge-stripe">
      <span class="yellow"></span><span class="blue"></span><span class="magenta"></span><span class="green"></span><span class="orange"></span>
    </div>

    <header class="brand">
      <div class="tooth-art" role="img" aria-label="Glossy white 3D tooth illustration"></div>
      <div class="brand-name">Brightpath Orthodontics</div>
    </header>

    <section class="doctor">
      <h1 class="doctor-name">Darren Holloway</h1>
      <p class="doctor-credentials">DDS, MSD</p>
    </section>

    <ul class="contact">
      <li>
        <svg viewBox="0 0 20 20" aria-hidden="true"><path fill="var(--blue)" d="M5 2l3 0 1.5 4-2 1.5c1 2 2.5 3.5 4.5 4.5l1.5-2 4 1.5 0 3c0 1-1 2-2 2C8 16.5 3.5 12 3 4c0-1 1-2 2-2z"/></svg>
        817-555-0143
      </li>
      <li>
        <svg viewBox="0 0 20 20" aria-hidden="true"><rect x="2" y="4" width="16" height="12" fill="var(--magenta)"/></svg>
        info@brightpathortho.example
      </li>
      <li>
        <svg viewBox="0 0 20 20" aria-hidden="true"><rect x="2.5" y="3" width="15" height="10" fill="none" stroke="var(--green)" stroke-width="2"/><path d="M7 17h6M10 13v4" stroke="var(--green)" stroke-width="2"/></svg>
        www.brightpathortho.example
      </li>
    </ul>

    <address class="address">
      5214 West Maple Avenue, Suite 204<br>
      Mansfield, TX 76099
    </address>
  </article>
</main>
</body>
</html>
```